International Trade Consulting Firm Seeks Quality Newsletter Design

Our company provides consulting services to Pinnacle 300 type companies. We compete with the largest consulting companies in the world. However, we have the highest level of expertise in the industry and need to look the most professional and high end. We have very relevant and important information to provide our customers about their compliance and projects. We will have the winning design coded to be an e-newsletter, so it needs to be one page. We want to keep our company colors and logo design in the newsletter, they are attached. We DO NOT want it to look like a mini-version of our website. We want a fresh look to this marketing piece. Newsletter will need to include title, possible sub-heading, space for a feature story, 2 other stories included, and space on either the left or right for short cuts, links or highlights of other articles. Contents/'In this issue' section, about us or branding area, section for relevant links, etc...
Target Market(s)
Pinnacle 300 companies, High-level management
Industry/Entity Type
Marketing

```html
<!DOCTYPE html>
<html lang="en">
<head>
<meta charset="utf-8">
<title>Newsletter</title>
<link href="https://fonts.googleapis.com/css2?family=Arimo:wght@400;700&family=Archivo+Narrow:wght@400&display=swap" rel="stylesheet">
<style>
:root{
  --topbar:#1f3551;
  --page:#254b6b;
  --footer:#1b2a3e;
  --panel:#1f3c57;
  --panel-edge:#17304a;
  --masthead:#b6c3cd;
  --heading-ink:#2e5878;
  --accent:#5aaee8;
  --link:#6cb8f0;
  --text:#ffffff;
  --muted:#4f8fc4;
  --rule:#2e4d6a;
  --tab-top:#3a8fd0;
  --tab-bottom:#1f6aa8;
  --tab-ink:#10263c;
  --footer-ink:#2f5274;
  --media-top:#3f7fae;
  --media-bottom:#2a5f88;
}
*{margin:0;padding:0;box-sizing:border-box}
html,body{width:1200px;height:1000px;overflow:hidden}
body{background:var(--page);font-family:"Arimo",Arial,sans-serif;position:relative;color:var(--text)}
.notice-bar{position:absolute;left:0;top:0;width:1200px;height:56px;background:var(--topbar);border-bottom:1px solid #2b5a85;text-align:center;font-size:12px;line-height:15px;color:var(--muted);padding-top:8px}
.notice-bar a{color:#a9d4f5}
.masthead{position:absolute;left:316px;top:77px;width:587px;height:75px;background:var(--masthead);border-radius:6px;box-shadow:0 2px 3px rgba(0,0,0,.35)}
.brand{position:absolute;left:3px;top:4px;width:195px;height:55px;background:#0c0c0c;display:flex;align-items:center;justify-content:center;gap:8px;font-weight:700;font-size:14px;color:#7dbb4a}
.brand-mark{width:10px;height:10px;background:#7dbb4a}
.masthead-title{position:absolute;left:254px;top:4px;font-size:30px;color:var(--heading-ink);letter-spacing:2px}
.masthead-sub{position:absolute;left:261px;top:47px;font-size:17px;color:var(--heading-ink);letter-spacing:.5px}
.panel{position:absolute;background:var(--panel);border:1px solid var(--panel-edge);border-radius:6px;box-shadow:inset 0 1px 0 rgba(255,255,255,.04)}
.feature{left:318px;top:193px;width:367px;height:645px;padding:20px 22px 0}
.story-title{font-size:19px;font-weight:700;color:var(--accent);margin-bottom:10px}
.body-copy{font-size:13px;line-height:16px;margin-bottom:9px;width:318px}
.body-copy.tight{width:305px}
.body-copy a,.brief a{color:var(--link)}
.rule{border:0;border-top:1px solid var(--rule);margin:18px -2px 20px}
.photo{width:322px;height:174px;background:linear-gradient(180deg,var(--media-top),var(--media-bottom));box-shadow:2px 2px 3px rgba(0,0,0,.5);margin-bottom:11px}
.bullets{list-style:none;margin-top:2px}
.bullets li{position:relative;padding-left:17px;font-size:13.5px;line-height:22px}
.bullets li::before{content:"";position:absolute;left:1px;top:9px;width:5px;height:5px;border-radius:50%;background:var(--accent);box-shadow:0 0 2px #8fd0ff}
.side-tab{position:absolute;left:-11px;width:211px;height:35px;background:linear-gradient(var(--tab-top),var(--tab-bottom));border-radius:3px 3px 0 0;box-shadow:0 3px 2px rgba(0,0,0,.45);font-size:16px;color:var(--tab-ink);padding:8px 10px;display:flex;justify-content:space-between;align-items:center}
.issue{left:706px;top:194px;width:194px;height:186px}
.issue .side-tab{top:18px}
.issue .bullets{position:absolute;top:73px;left:20px}
.issue .bullets li{font-size:13px;padding-left:19px}
.news{left:706px;top:401px;width:194px;height:410px}
.news .side-tab{top:18px}
.brief{position:absolute;left:20px;width:148px}
.brief-title{font-size:13px;font-weight:700;color:var(--accent);line-height:16px;margin-bottom:10px}
.brief p{font-size:12.5px;line-height:15px}
.brief-rule{position:absolute;left:20px;width:152px;border-top:1px solid var(--rule)}
.footer{position:absolute;left:0;top:858px;width:1200px;height:142px;background:var(--footer);border-top:1px solid #2b5a85}
.footer-address{position:absolute;left:371px;top:80px;font-family:"Archivo Narrow","Arial Narrow",sans-serif;font-size:21px;color:var(--footer-ink);text-shadow:0 1px 1px #000;letter-spacing:-.6px;white-space:nowrap;transform:scaleX(.86);transform-origin:left top}
.footer-contact{position:absolute;left:377px;top:104px;font-size:10px;color:var(--footer-ink);letter-spacing:.3px}
</style>
</head>
<body>
<div class="notice-bar">
  You're receiving this newsletter because you signed up for it<br>
  Having trouble reading this email? <a href="#">View it in your browser.</a> | <a href="#">Click here to unsubscribe.</a>
</div>

<header class="masthead">
  <div class="brand"><span class="brand-mark"></span>Harborline Trade Group</div>
  <div class="masthead-title">Heading</div>
  <div class="masthead-sub">sub-heading</div>
</header>

<main class="panel feature">
  <h2 class="story-title">Lorem ipsum dolar sit amet</h2>
  <p class="body-copy">Suspendisse potenti--Fusce eu ante in sapien vestibulum sagittis. Cras purus. Nunc rhoncus.</p>
  <p class="body-copy tight">Donec imperdiet, nibh sit amet pharetra placerat, tortor purus condimentum lectus, at <a href="#">dignissim nibh</a> velit vitae sem. Nunc condimentum blandit phasellus facilisis neque vitae purus.</p>
  <hr class="rule">
  <div class="photo" role="img" aria-label="Feature story photo"></div>
  <p class="body-copy">Suspendisse potenti--Fusce eu ante in sapien vestibulum sagittis. Cras purus. Nunc rhoncus.</p>
  <hr class="rule">
  <h2 class="story-title">Lorem ipsum dolar sit amet</h2>
  <p class="body-copy tight">Donec imperdiet, nibh sit amet pharetra placerat, tortor purus condimentum lectus, at dignissim nibh velit vitae sem. Nunc condimentum blandit phasellus facilisis neque vitae purus.</p>
  <ul class="bullets">
    <li>Aliquam lectus orci, adipiscing</li>
    <li>Aliquam lectus orci, adipiscing</li>
    <li>Aliquam lectus orci, adipiscing</li>
  </ul>
</main>

<aside class="panel issue">
  <div class="side-tab">In this issue
    <svg width="12" height="16" viewBox="0 0 12 16" aria-hidden="true"><circle cx="7" cy="2.5" r="2" fill="#10263c"/><path d="M4 6h5l-2.5 8h2l-.5 1.5H3l2.5-8H3.5z" fill="#10263c"/></svg>
  </div>
  <ul class="bullets">
    <li>Aliquam lectus orc</li>
    <li>Aliquam lectus orci</li>
    <li>Aliquam lectus orci</li>
    <li>Aliquam lectus orci</li>
  </ul>
</aside>

<aside class="panel news">
  <div class="side-tab">In other news
    <svg width="18" height="18" viewBox="0 0 18 18" aria-hidden="true"><circle cx="9" cy="9" r="8" fill="#1a3550"/><circle cx="9" cy="9" r="8" fill="none" stroke="#8fb6d8" stroke-width="1"/><ellipse cx="9" cy="9" rx="3.5" ry="8" fill="none" stroke="#8fb6d8" stroke-width="1"/><path d="M1 9h16" stroke="#8fb6d8"/></svg>
  </div>
  <article class="brief" style="top:78px">
    <h3 class="brief-title">Lorem ipsum dolar sit amet</h3>
    <p>Nunc ipsum metus, iaculis sit amet, interdum at. Donce imperiat ccumsan felis. <a href="#">dignissim nibh</a> Cras sed ante.</p>
  </article>
  <div class="brief-rule" style="top:215px"></div>
  <article class="brief" style="top:235px">
    <h3 class="brief-title">Lorem ipsum dolar sit amet</h3>
    <p>Nunc ipsum metus, iaculis sit amet, interdum at. Donce imperiat ccumsan felis. <a href="#">dignissim nibh</a> Cras sed ante.</p>
  </article>
  <div class="brief-rule" style="top:370px"></div>
</aside>

<footer class="footer">
  <div class="footer-address">Meridian Ledger LLC, 1270 North Alder Ave., Suite 310 Boulder, CO 80301</div>
  <div class="footer-contact">Tel:30355501 Fax 303555014</div>
</footer>
</body>
</html>
```